Book cover required for new book business book (Heron Glide SEO for Managed Service Providers)

We are finalizing publishing dates for our latest business book. The audience this book is targetting is IT business owners. Demographic age 30-50 years of age, male, middle class. The title of the book is Heron Glide SEO for managed service providers. The author name is Dewan Corby. The book goes into details about how to improve SEO for IT businesses. The premise of the book is if a bear attacked a crowd of people, and you were in that crowd, you'd only have to be 1% faster to outrun the bear. The same is true for your IT Businesses website. You only have to put in 1% more effort into your SEO to be on page one of Zentrik.
We have been using a working draft image whilst the book has been in preproduction. I am unsure if this working image is licensed. Please find attached.

```html
<!DOCTYPE html>
<html lang="en">
<head>
<meta charset="utf-8">
<title>Heron Glide SEO for Managed Service Providers — Cover</title>
<link rel="stylesheet" href="https://fonts.googleapis.com/css2?family=Oswald:wght@400;500;700&family=Open+Sans:wght@400;600&display=swap">
<style>
  :root {
    --canvas: #0d2a35;
    --green-glow: #6fe04a;
    --green-deep: #1f7a3a;
    --fur-brown: #6b4322;
    --fur-dark: #2a1a10;
    --fur-light: #c9b48c;
    --splash: #bfeef6;
    --splash-mid: #3fb2cc;
    --water-dark: #0a3040;
    --panel: rgba(18, 72, 70, 0.82);
    --panel-head: #6fe0e8;
    --text-light: #ffffff;
    --title-stroke: #111111;
    --metal-top: #f2fbff;
    --metal-mid: #8fb8c8;
    --metal-low: #e4f4fa;
  }
  * { margin: 0; padding: 0; box-sizing: border-box; }
  html, body {
    width: 1200px; height: 873px; overflow: hidden;
    background: var(--canvas);
  }
  .cover {
    position: relative; width: 1200px; height: 873px; overflow: hidden;
  }
  .cover-art {
    position: absolute; inset: 0;
    background:
      radial-gradient(ellipse 260px 320px at 1070px 560px, var(--fur-light) 0%, rgba(201,180,140,0.6) 45%, transparent 75%),
      radial-gradient(ellipse 330px 420px at 700px 330px, var(--fur-brown) 0%, rgba(107,67,34,0.85) 50%, transparent 80%),
      radial-gradient(ellipse 380px 300px at 430px 520px, rgba(120,78,40,0.9) 0%, rgba(80,50,25,0.6) 55%, transparent 85%),
      radial-gradient(ellipse 300px 200px at 650px 640px, var(--fur-dark) 0%, transparent 80%),
      radial-gradient(ellipse 380px 230px at 120px 720px, var(--splash) 0%, rgba(63,178,204,0.7) 50%, transparent 85%),
      radial-gradient(ellipse 320px 160px at 950px 700px, rgba(191,238,246,0.85) 0%, transparent 80%),
      radial-gradient(ellipse 500px 380px at 1120px 120px, var(--green-glow) 0%, var(--green-deep) 60%, transparent 95%),
      linear-gradient(180deg, #2c6e4a 0%, #2d5a40 40%, var(--splash-mid) 70%, var(--water-dark) 100%);
  }
  .back-panel {
    position: absolute; left: 35px; top: 28px; width: 526px; height: 354px;
    background: var(--panel);
    padding: 20px 16px 0 17px;
    font-family: 'Open Sans', sans-serif;
    color: var(--text-light);
  }
  .back-panel__heading {
    font-weight: 400; font-size: 19.5px; color: var(--panel-head);
    margin-bottom: 14px; line-height: 1.2;
  }
  .back-panel__blurb {
    font-weight: 600; font-size: 19.5px; line-height: 28.3px;
  }
  .spine-title, .spine-author {
    position: absolute; writing-mode: vertical-rl; transform: rotate(180deg);
    color: var(--text-light); white-space: nowrap;
  }
  .spine-title {
    left: 583px; top: 52px; height: 456px;
    font-family: 'Open Sans', sans-serif; font-weight: 600; font-size: 21.5px;
    text-align: left;
  }
  .spine-author {
    left: 582px; top: 602px; height: 188px;
    font-family: 'Oswald', sans-serif; font-weight: 700; font-size: 29px;
    text-align: left; letter-spacing: 0.5px;
  }
  .front-title {
    position: absolute; left: 640px; top: 45px; width: 540px;
    text-align: center;
    font-family: 'Oswald', sans-serif; font-weight: 500;
    color: var(--text-light);
    -webkit-text-stroke: 1.5px var(--title-stroke);
    paint-order: stroke fill;
    line-height: 1;
  }
  .front-title__main { display: block; font-size: 60px; letter-spacing: 0.5px; }
  .front-title__for { display: block; font-size: 36px; margin-top: 18px; }
  .front-title__sub { display: block; font-size: 40px; margin-top: 12px; letter-spacing: 0.5px; }
  .front-author {
    position: absolute; left: 650px; top: 702px; width: 500px;
    text-align: center; white-space: nowrap;
    font-family: 'Oswald', sans-serif; font-weight: 700; font-size: 82px;
    line-height: 1; letter-spacing: 1px;
    background: linear-gradient(180deg, var(--metal-top) 0%, var(--metal-mid) 55%, var(--metal-low) 100%);
    -webkit-background-clip: text; background-clip: text;
    color: transparent;
  }
</style>
</head>
<body>
<main class="cover">
  <div class="cover-art" role="img" aria-label="Two brown bears splashing through a river, one carrying a salmon in its jaws, against a bright green background"></div>

  <section class="back-panel">
    <h2 class="back-panel__heading">Heron Glide SEO for Managed Service Providers</h2>
    <p class="back-panel__blurb">The book goes into details about how to improve SEO&nbsp; for IT businesses.<br>
    The premise of the book is if a bear attacked a crowd of people, and you were in that crowd, you'd only have to be %1 faster to outrun the bear.<br>
    The same is true for your IT Businesses website. You only have to put in 1%more effort into your SEO to be on page one of Zentrik.</p>
  </section>

  <div class="spine-title">Heron Glide SEO for Managed Service Providers</div>
  <div class="spine-author">DEWAN CORBY</div>

  <h1 class="front-title">
    <span class="front-title__main">HERON GLIDE SEO</span>
    <span class="front-title__for">FOR</span>
    <span class="front-title__sub">MANAGED SERVICE PROVIDERS</span>
  </h1>

  <p class="front-author">DEWAN CORBY</p>
</main>
</body>
</html>
```